Mimi Harlan Poster

Need a design for poster for my daughter. Performer for school aged kids. Would like her name "MIMI or Mimi" on the poster- can change background

Target Market(s)

school aged kids

Industry/Entity Type

School

Requirements
Must have
• name - MIMI or Mimi on poster

```html
<!DOCTYPE html>
<html lang="en">
<head>
<meta charset="utf-8">
<title>Mimi Harlan Poster</title>
<link rel="stylesheet" href="https://fonts.googleapis.com/css2?family=Titan+One&family=Varela+Round&display=swap">
<style>
  :root {
    --paper: #ffffff;
    --flame-light: #ffb030;
    --flame: #f46a10;
    --flame-deep: #c8200a;
    --ember: #7a0c05;
    --night-top: #6a1a06;
    --night: #2a0a03;
    --night-deep: #140401;
    --frame: #f7881a;
    --frame-light: #ffb84a;
    --gold: #e0a838;
    --text: #ffffff;
    --accent: #ffd21a;
  }
  html, body {
    margin: 0;
    padding: 0;
    width: 1200px;
    height: 2308px;
    overflow: hidden;
    background: var(--paper);
  }
  .poster {
    position: absolute;
    left: 46px;
    top: 39px;
    width: 1108px;
    height: 2230px;
    overflow: hidden;
    background:
      radial-gradient(ellipse 70% 40% at 50% 35%, var(--flame-light) 0%, transparent 60%),
      radial-gradient(ellipse 90% 60% at 80% 55%, var(--flame) 0%, transparent 70%),
      linear-gradient(160deg, var(--flame-deep) 0%, var(--flame) 35%, var(--flame-deep) 75%, var(--ember) 100%);
  }
  .swirl {
    position: absolute;
    left: 0;
    top: 0;
    width: 1108px;
    height: 1700px;
  }
  .title {
    position: absolute;
    left: 0;
    right: 0;
    top: 95px;
    margin: 0;
    text-align: center;
    font-family: "Titan One", sans-serif;
    font-weight: 400;
    font-size: 260px;
    line-height: 1;
    letter-spacing: 14px;
    color: #fff6ea;
    -webkit-text-stroke: 6px #f08a2a;
    text-shadow:
      0 6px 0 #e06a18,
      0 12px 0 #b8400c,
      0 22px 30px rgba(90, 10, 0, 0.55);
  }
  .photo-frame {
    position: absolute;
    left: 128px;
    top: 433px;
    width: 840px;
    height: 1154px;
    box-sizing: border-box;
    border: 36px solid var(--frame);
    border-image: linear-gradient(135deg, var(--frame-light), var(--frame) 50%, #e8660c) 1;
    box-shadow: 0 10px 40px rgba(60, 5, 0, 0.5);
  }
  .photo {
    width: 100%;
    height: 100%;
    background:
      radial-gradient(ellipse 45% 55% at 50% 45%, #c89a3a 0%, transparent 70%),
      linear-gradient(180deg, #4a3a24 0%, #6a4a2a 45%, #8a8478 80%, #6f6b62 100%);
  }
  .info {
    position: absolute;
    left: 0;
    top: 1587px;
    width: 1108px;
    height: 643px;
    background: linear-gradient(180deg, var(--night-top) 0%, var(--night) 35%, var(--night-deep) 100%);
  }
  .flourish {
    position: absolute;
    left: 220px;
    width: 668px;
    height: 40px;
  }
  .flourish--top { top: 145px; }
  .flourish--bottom { top: 525px; }
  .details {
    position: absolute;
    left: 0;
    right: 0;
    top: 215px;
    margin: 0;
    text-align: center;
    font-family: "Varela Round", sans-serif;
    color: var(--text);
    font-size: 42px;
    line-height: 58px;
  }
  .details p { margin: 0; }
  .details .audience {
    color: var(--accent);
    font-size: 58px;
    line-height: 70px;
    margin-bottom: 14px;
  }
</style>
</head>
<body>
  <main class="poster">
    <svg class="swirl" viewBox="0 0 1108 1700" aria-hidden="true">
      <defs>
        <radialGradient id="glow" cx="50%" cy="50%" r="50%">
          <stop offset="0%" stop-color="#ffd070" stop-opacity="0.55"/>
          <stop offset="100%" stop-color="#ffd070" stop-opacity="0"/>
        </radialGradient>
      </defs>
      <ellipse cx="554" cy="360" rx="520" ry="220" fill="url(#glow)"/>
      <path d="M980 500 C1160 760 1120 1200 900 1480" fill="none" stroke="#ffb040" stroke-opacity="0.45" stroke-width="26"/>
      <path d="M1030 460 C1220 800 1160 1260 940 1560" fill="none" stroke="#ffd080" stroke-opacity="0.3" stroke-width="10"/>
      <path d="M120 1500 C-40 1200 -20 800 140 520" fill="none" stroke="#ff9a30" stroke-opacity="0.3" stroke-width="18"/>
    </svg>

    <h1 class="title">MIMI</h1>

    <figure class="photo-frame" style="margin:0">
      <div class="photo" role="img" aria-label="Photo of Mimi Harlan smiling, seated on a low stone wall outdoors"></div>
    </figure>

    <section class="info">
      <svg class="flourish flourish--top" viewBox="0 0 668 40" aria-hidden="true">
        <line x1="0" y1="20" x2="270" y2="20" stroke="var(--gold)" stroke-width="3"/>
        <line x1="398" y1="20" x2="668" y2="20" stroke="var(--gold)" stroke-width="3"/>
        <rect x="290" y="6" width="88" height="28" rx="14" fill="var(--gold)" opacity="0.8"/>
      </svg>

      <div class="details">
        <p>Will be from ages 5 to 17 yrs old.</p>
        <p class="audience">(boys and girls)</p>
        <p>Give-a-ways from Mimi to her fans</p>
        <p>No date- will be</p>
        <p>given away all year long.</p>
      </div>

      <svg class="flourish flourish--bottom" viewBox="0 0 668 40" aria-hidden="true">
        <line x1="0" y1="20" x2="270" y2="20" stroke="var(--gold)" stroke-width="3"/>
        <line x1="398" y1="20" x2="668" y2="20" stroke="var(--gold)" stroke-width="3"/>
        <rect x="290" y="6" width="88" height="28" rx="14" fill="var(--gold)" opacity="0.8"/>
      </svg>
    </section>
  </main>
</body>
</html>
```